IT Consulting Business Card Design

We need a business card on our company name....which is a IT consulting and staffing company. We also train masters graduates in various IT courses. 70% of the time these cards will be handed out to the graduate students at the universities. 30% for our clients and business partners. We are uploading our company logo...would like to see something that matches our logo or blends with it. Please visit www.brivolentaxis.com for more details on logo and colors.

Target Market(s)

70% of the time these cards will be handed out to the graduate students at the universities. 30% for our clients and business partners.

Industry/Entity Type

Business

Contact Information for Business Card

Tomas Verlinde
Vice-President
Brivolen Taxis Inc
3187 Corwick Lane, Suite 412
Dellmont Heights, NJ 07190
tomas@brivolentaxis.com
Office : 1-855-555-0148 X 312
Cell number : 908-555-0193

Requirements
Nice to have
• may be company logo and name on the back of the card and detials on the other side...just a thought..!!

```html
<!DOCTYPE html>
<html lang="en">
<head>
<meta charset="utf-8">
<title>Brivolen Taxis – Business Card</title>
<link href="https://fonts.googleapis.com/css2?family=Source+Sans+3:wght@400;600;700&display=swap" rel="stylesheet">
<style>
  :root {
    --stage: #2b2b2b;
    --red: #d81f26;
    --red-deep: #a8121a;
    --red-light: #ee3a3f;
    --white: #ffffff;
    --ink: #3a3a3a;
    --swoosh: #4a4a4a;
    --swoosh-light: #9a9a9a;
  }
  * { margin: 0; padding: 0; box-sizing: border-box; }
  html, body { width: 1200px; height: 716px; overflow: hidden; }
  body {
    background: var(--stage);
    font-family: "Source Sans 3", "Myriad Pro", sans-serif;
    position: relative;
  }
  .card {
    position: absolute;
    top: 208px;
    width: 520px;
    height: 300px;
    border-radius: 26px;
    overflow: hidden;
  }
  .card--front {
    left: 60px;
    background: linear-gradient(150deg, var(--red-light) 0%, var(--red) 45%, var(--red-deep) 100%);
  }
  .card--back { left: 620px; background: var(--white); }

  .front-pattern {
    position: absolute;
    inset: 0;
    background:
      radial-gradient(ellipse 60% 70% at 72% 30%, rgba(255,255,255,0.22), rgba(255,255,255,0) 70%),
      radial-gradient(ellipse 45% 40% at 20% 85%, rgba(255,255,255,0.14), rgba(255,255,255,0) 70%);
  }
  .front-brand {
    position: absolute;
    left: 60px;
    top: 106px;
    display: flex;
    align-items: center;
    gap: 12px;
  }
  .brand-dot {
    width: 42px; height: 42px; border-radius: 50%;
    background: var(--white);
  }
  .front-brand .brand-name {
    color: var(--white);
    font-weight: 700;
    font-size: 27px;
    letter-spacing: 0.5px;
  }
  .front-web {
    position: absolute;
    left: 116px;
    top: 168px;
    color: var(--white);
    font-size: 12px;
  }

  .back-shapes { position: absolute; inset: 0; }
  .back-brand {
    position: absolute;
    left: 150px;
    top: 42px;
    display: flex;
    align-items: center;
    gap: 12px;
  }
  .back-brand .brand-dot { background: var(--red); width: 48px; height: 48px; }
  .back-brand .brand-name {
    color: var(--red);
    font-weight: 700;
    font-size: 28px;
    letter-spacing: 0.5px;
  }
  .contact {
    position: absolute;
    left: 26px;
    top: 160px;
    color: var(--white);
    font-size: 12px;
    line-height: 15px;
  }
  .contact .person-name { font-size: 14px; letter-spacing: 0.5px; }
  .contact .person-title { margin-bottom: 8px; }
  .contact-line { display: flex; align-items: center; gap: 6px; }
  .contact-line svg { width: 10px; height: 10px; fill: var(--white); flex: none; }
  .contact-line.web { padding-left: 16px; }
  .address {
    position: absolute;
    right: 30px;
    bottom: 22px;
    text-align: right;
    color: var(--white);
    font-size: 13px;
    line-height: 17px;
  }
</style>
</head>
<body>

<section class="card card--front" aria-label="Card front">
  <div class="front-pattern" role="img" aria-label="Soft halftone dot pattern in light red tones"></div>
  <div class="front-brand">
    <span class="brand-dot"></span>
    <span class="brand-name">BRIVOLEN TAXIS</span>
  </div>
  <p class="front-web">www.brivolentaxis.com</p>
</section>

<section class="card card--back" aria-label="Card back">
  <svg class="back-shapes" viewBox="0 0 520 300" width="520" height="300" preserveAspectRatio="none" aria-hidden="true">
    <defs>
      <linearGradient id="backRed" x1="0" y1="0" x2="1" y2="1">
        <stop offset="0" stop-color="#e42a30"/>
        <stop offset="1" stop-color="#b5141b"/>
      </linearGradient>
    </defs>
    <path d="M0,118 C150,98 300,212 520,182 L520,200 C300,232 150,120 0,142 Z" fill="var(--swoosh-light)"/>
    <path d="M0,128 C150,108 300,222 520,192 L520,204 C300,234 150,124 0,146 Z" fill="var(--swoosh)"/>
    <path d="M0,142 C150,120 300,232 520,200 L520,300 L0,300 Z" fill="url(#backRed)"/>
  </svg>

  <div class="back-brand">
    <span class="brand-dot"></span>
    <span class="brand-name">BRIVOLEN TAXIS</span>
  </div>

  <div class="contact">
    <p class="person-name">TOMAS VERLINDE</p>
    <p class="person-title">Vice-President</p>
    <p class="contact-line">
      <svg viewBox="0 0 10 10"><path d="M2 0.5 L3.6 2.6 L2.6 3.6 C3.2 5 5 6.8 6.4 7.4 L7.4 6.4 L9.5 8 L8.3 9.5 C4.5 9 1 5.5 0.5 1.7 Z"/></svg>
      1-855-555-0148 X 312
    </p>
    <p class="contact-line">
      <svg viewBox="0 0 10 10"><path d="M2.5 0 H7.5 V10 H2.5 Z M3.3 1 V8 H6.7 V1 Z"/></svg>
      908-555-0193
    </p>
    <p class="contact-line">
      <svg viewBox="0 0 10 10"><path d="M0 2 H10 V8.5 H0 Z M0.8 2.6 L5 5.6 L9.2 2.6 Z" fill-rule="evenodd"/></svg>
      tomas@brivolentaxis.com
    </p>
    <p class="contact-line web">www.brivolentaxis.com</p>
  </div>

  <div class="address">
    <p>Brivolen Taxis Inc</p>
    <p>3187 Corwick Lane,</p>
    <p>Suite 412 Dellmont Heights, NJ 07190</p>
  </div>
</section>

</body>
</html>
```